Plume - Stationary Design/Layout

We are a well established clothing design and manufacturing company (Plume Sourcing) based in London UK, with our own factory in Bangladesh, supplying to many fashion retailers and brands. Our factory has very high environmental and ethical standards with people at its heart. Our quality of garments are second to none.
Our new logo has been proudly developed by the Pixel Guild community last month, we are now in the second phase and need the layout designed for our letterheads, double sided business cards, compliment slip and clothing ticket. Feel as creative as you like, but make sure it looks great!!
***The Logo - the logo design and colour is set and should NOT be changed and stay on a dark grey backround. The logo artwork to use is attached.
***Details to use for the business card:
Dorian Hartley
Direct Line: 020 7946 0518
dorian@plumesourcing-mail.test
Plume Sourching Ltd.
58 - 60 Fenwick Row
Harwick . Brookdale
NW3 5QJ
Switchboard: 020 7946 0733
Fax: 020 7946 0733
www.plumesourcing-mail.test
***Details to use for the letterhead and compliment slip:
Plume Sourching Ltd.
58 - 60 Fenwick Row
Harwick . Brookdale
NW3 5QJ
Fax: 020 7946 0733
www.plumesourcing-mail.test
***Details for Swing Ticket:
Size: 12cm height by 5.5cm width
One side need to have just the logo without the 'Sourcing', on the other it needs to stay blank

```html
<!DOCTYPE html>
<html lang="en">
<head>
<meta charset="utf-8">
<title>Plume Sourcing – Stationery Layout</title>
<link rel="stylesheet" href="https://fonts.googleapis.com/css2?family=Didact+Gothic&family=Questrial&display=swap">
<style>
  :root {
    --forest: #2e3a20;
    --sage: #8aad72;
    --paper: #ffffff;
    --ink: #2e3a20;
    --label: #1a1a1a;
    --name-ink: #111111;
  }
  * { margin: 0; padding: 0; box-sizing: border-box; }
  html, body { width: 849px; height: 1200px; overflow: hidden; background: var(--paper); }
  body { position: relative; font-family: "Didact Gothic", "Questrial", sans-serif; color: var(--ink); }

  .label { position: absolute; font-size: 13px; color: var(--label); line-height: 16px; }

  .piece { position: absolute; background: var(--forest); }
  .frame { position: absolute; background: var(--sage); }
  .sheet { position: absolute; background: var(--paper); }

  .brand-block {
    position: absolute; background: var(--forest);
    display: flex; align-items: center; justify-content: center;
    color: var(--sage); white-space: nowrap; overflow: hidden;
  }

  .text { position: absolute; white-space: nowrap; }
  .text strong { font-weight: 700; }
  .dot { color: var(--sage); }

  /* Compliment slip */
  .slip-heading { left: 85px; top: 109px; font-size: 14px; font-weight: 700; letter-spacing: .3px; }
  .slip-address { left: 546px; top: 190px; font-size: 13px; line-height: 19.5px; }
  .slip-address .gap { height: 19px; }

  /* Business cards */
  .card-text { font-size: 8.5px; line-height: 11px; }
  .card-name { font-size: 12px; color: var(--name-ink); }
  .card-name strong { font-weight: 700; }

  /* Swing tickets */
  .ticket-brand { font-size: 96px; letter-spacing: 6px; }
</style>
</head>
<body>

<!-- Compliment slip -->
<div class="label" style="left:10px;top:5px;">Comp. Slip 99 x 210</div>
<section class="comp-slip">
  <div class="piece" style="left:0;top:28px;width:827px;height:390px;"></div>
  <div class="frame" style="left:38px;top:67px;width:750px;height:311px;"></div>
  <div class="sheet" style="left:50px;top:79px;width:726px;height:287px;"></div>
  <div class="text slip-heading">WITH COMPLIMENTS</div>
  <div class="brand-block" style="left:546px;top:111px;width:198px;height:66px;font-size:22px;">Plume Sourcing</div>
  <div class="text slip-address">
    <div><strong>Plume Sourching Ltd.</strong></div>
    <div>58 - 60 Fenwick Row</div>
    <div>Harwick <span class="dot">•</span> Brookdale <span class="dot">•</span> NW3 5QJ</div>
    <div class="gap"></div>
    <div><strong>Switchboard:</strong> 020 7946 0733</div>
    <div><strong>Fax:</strong> 020 7946 0733</div>
    <div>www.plumesourcing-mail.test</div>
  </div>
</section>

<!-- Business card, layout A -->
<section class="business-card card-a">
  <div class="piece" style="left:58px;top:439px;width:335px;height:217px;"></div>
  <div class="frame" style="left:76px;top:457px;width:299px;height:181px;"></div>
  <div class="sheet" style="left:82px;top:463px;width:287px;height:169px;"></div>
  <div class="text card-text" style="left:95px;top:482px;">
    <div><strong>Direct Line:</strong> 020 7946 0518</div>
    <div>dorian@plumesourcing-mail.test</div>
  </div>
  <div class="text card-name" style="left:95px;top:529px;">Dorian <strong>Hartley</strong></div>
  <div class="brand-block" style="left:235px;top:481px;width:116px;height:38px;font-size:12.5px;">Plume Sourcing</div>
  <div class="text card-text" style="left:235px;top:530px;">
    <div><strong>Plume Sourching Ltd.</strong></div>
    <div>58 - 60 Fenwick Row</div>
    <div>Harwick <span class="dot">•</span> Brookdale</div>
    <div>NW3 5QJ</div>
    <div style="height:11px;"></div>
    <div><strong>Switchboard:</strong> 020 7946 0733</div>
    <div><strong>Fax:</strong> 020 7946 0733</div>
    <div>www.plumesourcing-mail.test</div>
  </div>
</section>

<!-- Business card, layout B -->
<section class="business-card card-b">
  <div class="piece" style="left:425px;top:439px;width:335px;height:217px;"></div>
  <div class="frame" style="left:443px;top:457px;width:299px;height:181px;"></div>
  <div class="sheet" style="left:449px;top:463px;width:287px;height:169px;"></div>
  <div class="text card-name" style="left:462px;top:529px;">Dorian <strong>Hartley</strong></div>
  <div class="text card-text" style="left:462px;top:596px;">
    <div><strong>Direct Line:</strong> 020 7946 0518</div>
    <div>dorian@plumesourcing-mail.test</div>
  </div>
  <div class="brand-block" style="left:603px;top:481px;width:115px;height:38px;font-size:12.5px;">Plume Sourcing</div>
  <div class="text card-text" style="left:602px;top:530px;">
    <div><strong>Plume Sourching Ltd.</strong></div>
    <div>58 - 60 Fenwick Row</div>
    <div>Harwick <span class="dot">•</span> Brookdale</div>
    <div>NW3 5QJ</div>
    <div style="height:11px;"></div>
    <div><strong>Switchboard:</strong> 020 7946 0733</div>
    <div><strong>Fax:</strong> 020 7946 0733</div>
    <div>www.plumesourcing-mail.test</div>
  </div>
</section>
<div class="label" style="left:178px;top:661px;">Business Card 55 x 85</div>

<!-- Swing ticket -->
<div class="label" style="left:20px;top:764px;">Swing Ticket 120 x 55</div>
<section class="swing-ticket">
  <div class="piece" style="left:178px;top:692px;width:473px;height:217px;"></div>
  <div class="frame" style="left:200px;top:714px;width:429px;height:173px;"></div>
  <div class="sheet" style="left:208px;top:722px;width:413px;height:157px;"></div>
  <div class="text ticket-brand" style="left:208px;top:722px;width:413px;height:157px;display:flex;align-items:center;justify-content:center;color:var(--sage);">Plume</div>
</section>

<!-- Swing ticket Mk2 -->
<div class="label" style="left:20px;top:990px;">Swing Ticket 120 x 55<br>Mk2</div>
<section class="swing-ticket mk2">
  <div class="piece" style="left:178px;top:926px;width:473px;height:217px;"></div>
  <div class="frame" style="left:200px;top:948px;width:429px;height:173px;"></div>
  <div class="sheet" style="left:208px;top:956px;width:413px;height:157px;"></div>
  <div class="brand-block" style="left:259px;top:981px;width:309px;height:106px;font-size:76px;letter-spacing:5px;">Plume</div>
</section>

</body>
</html>
```